Website plus logo for a finance business (in Wix)

We need a revamp of our website and our logo - visit www.falconlending.com for the current site.

We are a relatively new finance firm, providing short term (bridging) loans to property developers and other businesses in the UK.

Most of the information will go on the homepage. The other 3 or 4 pages are relatively basic. If you felt it was appropriate, the information on page 2 (case studies) could be incorporated on page 1.

The current website isn't too bad and gives you an idea of the information we would like covering on the website and in what order.

The logo should be clean, simple and modern, probably branded around a rocket. The current logo is a good starting point. The word rocket should be the focal point though.

The main header colour scheme should be similar to the current website (deep purples) but we would consider dark blues or reds. An example of a palette of colours we really like is attached.

The style should be modern and clean. Lots of whites and background space but with an underlying warmth, suggesting trust and reliability.

Examples of good brands and websites that we like in our sector are www.harborfunds.com, www.sagelending.co.uk and www.corvelle.co.uk - we particularly like Corvelle.

Important note - as part of the service, the website designer must be able to create the website in Wix once the design is approved. Our current website is through Wix and we want to keep it that way.

Therefore, once the design is approved, as part of the finalisation process, the designer will need to create the website in our existing Wix account.

This will also involve creating a mobile friendly version of the site (which is more or less automatic in Wix anyway). None of this should be difficult as Wix is very easy to use.

Thanks for your interest!

Kind regards

FalconLending

Target Market(s)

Small to medium property developers and businesses in the North West of the UK

Industry/Entity Type

Finance

Contact Information for Business Card

One side just feature the logo against a strong background colour.
The other side should have a nice clean look about it, with the details of our sales director, Nadia Pemberton.
nadia@falconlending.com
0161 482 9153
07931 604718

Logo Text

Falcon Lending

Coding

Coded - Design and coding required

Number of Pages Required

4 page

Font styles to use
Sans Serif

Colors
6b449b
0456a4

Requirements
Must have
• Clean looking home page, modelled on the examples that we've given.
• The start of the home page must make it clear what we do - this could be achieved by rotating banners.
• Must be produced in Wix once the design is approved.
• Should follow example colour palette given.
Nice to have
• Parallax pictures
Should not have
• Old fashioned or traditional styling - we do not want to look like an accountant or law firm's website

```html
<!DOCTYPE html>
<html lang="en">
<head>
<meta charset="utf-8">
<title>Falcon Lending – Bridging Loans</title>
<link href="https://fonts.googleapis.com/css2?family=Rubik:wght@300;400;500&display=swap" rel="stylesheet">
<style>
:root{
  --ink:#3a3a3a;
  --muted:#6d6d6d;
  --accent:#e8506d;
  --accent-soft:#f3a3b3;
  --brand:#6b449b;
  --footer:#3b1f55;
  --band:#ececec;
  --white:#ffffff;
}
*{box-sizing:border-box;margin:0;padding:0}
html,body{width:1200px;height:2944px;overflow:hidden;background:var(--white)}
body{font-family:"Rubik",Arial,sans-serif;color:var(--ink);position:relative}
.abs{position:absolute}

.logo{left:128px;top:26px;display:flex;align-items:center;gap:10px}
.logo-dot{width:22px;height:22px;border-radius:50%;background:var(--brand)}
.logo-name{font-size:26px;font-weight:500;color:var(--brand)}

.nav{right:130px;top:38px;display:flex;gap:30px;font-size:15px;color:var(--muted)}
.nav .active{color:var(--accent);text-decoration:underline}
.nav .phone{color:var(--accent)}

.hero-title{left:130px;top:112px;width:900px;font-size:68px;font-weight:300;line-height:80px;color:var(--ink)}

.section-title{font-weight:300;color:var(--ink)}
.about-title{left:284px;top:668px;font-size:46px;z-index:2;white-space:nowrap}
.about-photo{left:400px;top:660px;width:400px;height:384px;z-index:1;background:linear-gradient(135deg,#c9a48a,#8a6a5c 55%,#4f4a55)}
.about-copy{left:400px;top:1068px;width:400px;font-size:14px;line-height:22px;color:var(--muted)}
.about-copy p{margin-bottom:16px}
.read-more{left:400px;top:1228px;font-size:15px;color:var(--accent)}

.help-title{left:0;width:1200px;top:1320px;text-align:center;font-size:64px}

.service{width:420px}
.service-head{display:flex;align-items:center;gap:14px;margin-bottom:14px}
.service-head svg{width:58px;height:58px;flex:none}
.service-name{font-size:34px;font-weight:300;color:var(--accent)}
.service p{font-size:14px;line-height:22px;color:var(--muted);margin-bottom:14px;padding-left:72px}

.band{left:0;top:2012px;width:1200px;height:528px;background:var(--band)}
.best-title{left:0;width:1200px;top:2080px;text-align:center;font-size:64px}
.partners{left:130px;top:2190px;width:940px;display:flex;justify-content:space-between;font-size:18px;font-weight:500;color:#333;letter-spacing:1px}
.quote-by{left:0;width:1200px;top:2312px;text-align:center;font-size:16px;color:var(--muted)}
.quote{left:290px;width:620px;top:2344px;text-align:center;font-size:20px;line-height:32px;color:var(--ink);font-weight:300}
.dots{left:563px;top:2450px;display:flex;gap:12px}
.dots span{width:11px;height:11px;border-radius:50%;background:#999}
.dots span:first-child{background:var(--accent)}
.dots span:nth-child(2){background:#c0283f}

.footer{left:0;top:2540px;width:1200px;height:404px;background:var(--footer);color:var(--white)}
.contact-name{left:130px;top:62px;font-size:28px;font-weight:400}
.contact-role{left:130px;top:104px;width:210px;font-size:12px;line-height:18px;color:#d8cde4}
.field-label{font-size:12px;color:#e6ddef}
.field-line{height:1px;background:#b9a9cc}
.send{left:796px;top:240px;font-size:13px;color:#e6ddef}
.copyright{left:130px;top:330px;font-size:11px;color:#cbbcdb}
.social{right:130px;top:326px;display:flex;gap:14px}
.social span{width:14px;height:14px;border-radius:50%;background:var(--white)}
</style>
</head>
<body>

<header>
  <div class="abs logo"><span class="logo-dot"></span><span class="logo-name">Falcon Lending</span></div>
  <nav class="abs nav">
    <span class="active">Home</span><span>Case studies</span><span>FAQs</span><span>Intermediaries</span><span>Contact</span><span class="phone">0161 482 9153</span>
  </nav>
</header>

<h1 class="abs hero-title">Falcon Lending is a Manchester-based bridging loan provider, covering property purchases, developments and general business needs.</h1>

<section class="about">
  <div class="abs about-photo" role="img" aria-label="Portrait photograph of a smiling team member"></div>
  <h2 class="abs section-title about-title">About Us</h2>
  <div class="abs about-copy">
    <p>We are not a broker. We fund you with our own money. When you speak to us, you speak with the decision maker.</p>
    <p>We do not have strict lending parameters. We pride ourselves on working out an individual deal for each client. We can find solutions for most clients, large or small.</p>
  </div>
  <span class="abs read-more">Read More</span>
</section>

<section class="help">
  <h2 class="abs section-title help-title">How can we help?</h2>

  <div class="abs service" style="left:140px;top:1460px">
    <div class="service-head">
      <svg viewBox="0 0 58 58" fill="none" stroke="var(--accent-soft)" stroke-width="2"><rect x="6" y="14" width="46" height="32" rx="3"/><line x1="6" y1="24" x2="52" y2="24"/><line x1="12" y1="36" x2="26" y2="36"/></svg>
      <span class="service-name">Bridging loans</span>
    </div>
    <p>Do you need to put in place temporary funding whilst you organise a long term strategy?</p>
    <p>Falcon can provide bridge funding on a wide range of residential and commercial property throughout England and Wales.</p>
  </div>

  <div class="abs service" style="left:690px;top:1460px">
    <div class="service-head">
      <svg viewBox="0 0 58 58" fill="none" stroke="var(--accent-soft)" stroke-width="2"><rect x="10" y="10" width="22" height="12" rx="2" transform="rotate(-40 21 16)"/><line x1="24" y1="24" x2="46" y2="46"/><line x1="8" y1="50" x2="30" y2="50"/></svg>
      <span class="service-name">Auction purchases</span>
    </div>
    <p>Thinking of bidding? Won a property?</p>
    <p>Falcon is able to swiftly fund the purchase of an auction property whilst you organise long term funding. Falcon can provide finance to help with the development of property.</p>
    <p>We can supply the acquisition funding and/or a facility to be drawn down as work progresses.</p>
  </div>

  <div class="abs service" style="left:140px;top:1772px">
    <div class="service-head">
      <svg viewBox="0 0 58 58" fill="none" stroke="var(--accent-soft)" stroke-width="2"><rect x="6" y="18" width="46" height="30" rx="3"/><path d="M22 18v-6h14v6"/><line x1="6" y1="30" x2="52" y2="30"/></svg>
      <span class="service-name">Business loans</span>
    </div>
    <p>Do you want to grow your business?</p>
    <p>We provide short term facilities allowing you to achieve your ambitions.</p>
  </div>

  <div class="abs service" style="left:690px;top:1772px">
    <div class="service-head">
      <svg viewBox="0 0 58 58" fill="none" stroke="var(--accent-soft)" stroke-width="2"><path d="M8 48h42M14 48V26l15-12 15 12v22"/><rect x="24" y="34" width="10" height="14"/></svg>
      <span class="service-name">Development</span>
    </div>
    <p>Falcon can provide finance to help with the development of property.</p>
    <p>We can supply the acquisition funding and/or a facility to be drawn down as work progresses.</p>
  </div>
</section>

<section>
  <div class="abs band"></div>
  <h2 class="abs section-title best-title">Recommended by the Best.</h2>
  <div class="abs partners">
    <span>Coralyn</span><span>Harwick</span><span>Swellmark</span><span>Brennock</span><span>Tidewell</span><span>Lumo</span><span>Ravello</span>
  </div>
  <p class="abs quote-by">Mr G. Developer</p>
  <p class="abs quote">“ Dealing with Nadia was a pleasure. She's always on the end of the phone. I always felt like a valued client and not just a number. ”</p>
  <div class="abs dots"><span></span><span></span><span></span></div>
</section>

<footer class="abs footer">
  <h3 class="abs contact-name">Nadia Pemberton</h3>
  <p class="abs contact-role">Nadia is our Client Manager and will be your first point of contact.</p>

  <span class="abs field-label" style="left:556px;top:86px">Name</span>
  <div class="abs field-line" style="left:556px;top:110px;width:250px"></div>
  <span class="abs field-label" style="left:840px;top:86px">Email</span>
  <div class="abs field-line" style="left:840px;top:110px;width:230px"></div>
  <span class="abs field-label" style="left:556px;top:138px">Message</span>
  <div class="abs field-line" style="left:556px;top:216px;width:514px"></div>
  <span class="abs send">Send</span>

  <p class="abs copyright">Copyright © 2018 Falcon Lending. All rights reserved.</p>
  <div class="abs social"><span></span><span></span><span></span></div>
</footer>

</body>
</html>
```